Business Cards

Need a neat design for a new business card

Industry/Entity Type

Residential Construction

Contact Information for Business Card

Company Name- KOVE Construction Inc.
Owner- Marcus Tolliver
Phone number- (555)203-7481
Email- kovecohomes@brindlemail.example
Facebook- www.socialpage.example/kovecohomes

Colors
fefdec

```html
<!DOCTYPE html>
<html lang="en">
<head>
<meta charset="utf-8">
<title>KOVE Construction Business Card</title>
<link rel="stylesheet" href="https://fonts.googleapis.com/css2?family=Cormorant+Garamond:wght@500;700&family=Arimo:wght@400&display=swap">
<style>
  :root {
    --stage: #2b2b2b;
    --card-cream: #fefdec;
    --card-black: #151515;
    --ink: #151515;
    --line-light: #e8e8e8;
  }
  * { margin: 0; padding: 0; box-sizing: border-box; }
  html, body { width: 1200px; height: 900px; overflow: hidden; }
  body {
    background: var(--stage);
    display: flex;
    flex-direction: column;
    align-items: center;
    justify-content: center;
    gap: 40px;
  }
  .card {
    width: 700px;
    height: 400px;
    position: relative;
    box-shadow: 0 8px 24px rgba(0,0,0,0.45);
  }

  /* Front */
  .card--front { background: var(--card-cream); color: var(--ink); }
  .brand {
    position: absolute;
    top: 62px;
    left: 0;
    width: 100%;
    display: flex;
    align-items: center;
    justify-content: center;
    gap: 16px;
  }
  .brand__square { width: 14px; height: 14px; background: var(--ink); }
  .brand__name {
    font-family: "Cormorant Garamond", serif;
    font-weight: 500;
    font-size: 56px;
    letter-spacing: 4px;
    line-height: 1;
  }
  .brand__sub {
    position: absolute;
    top: 128px;
    width: 100%;
    text-align: center;
    font-family: "Cormorant Garamond", serif;
    font-weight: 500;
    font-size: 20px;
    letter-spacing: 6px;
  }
  .owner {
    position: absolute;
    top: 222px;
    right: 410px;
    text-align: right;
  }
  .owner__name {
    font-family: "Cormorant Garamond", serif;
    font-weight: 700;
    font-size: 26px;
    letter-spacing: 1px;
  }
  .owner__role {
    font-family: "Arimo", sans-serif;
    font-size: 14px;
    letter-spacing: 2px;
    margin-top: 4px;
  }
  .divider {
    position: absolute;
    top: 212px;
    left: 310px;
    width: 1px;
    height: 110px;
    background: var(--ink);
  }
  .contacts {
    position: absolute;
    top: 222px;
    left: 330px;
    list-style: none;
    font-family: "Arimo", sans-serif;
    font-size: 16px;
  }
  .contacts li {
    display: flex;
    align-items: center;
    gap: 10px;
    margin-bottom: 9px;
  }
  .contacts svg { width: 20px; height: 20px; flex: none; }

  /* Back */
  .card--back { background: var(--card-black); color: var(--line-light); }
  .back__border {
    position: absolute;
    inset: 26px;
    border: 1px solid var(--line-light);
  }
  .back__frame {
    position: absolute;
    left: 50%;
    top: 50%;
    transform: translate(-50%, -50%);
    border: 1px solid var(--line-light);
    padding: 20px 44px 16px;
    text-align: center;
  }
  .back__name {
    font-family: "Cormorant Garamond", serif;
    font-weight: 500;
    font-size: 60px;
    letter-spacing: 6px;
    line-height: 1;
  }
  .back__sub {
    font-family: "Cormorant Garamond", serif;
    font-weight: 500;
    font-size: 16px;
    letter-spacing: 6px;
    margin-top: 8px;
  }
</style>
</head>
<body>
  <section class="card card--front">
    <div class="brand">
      <span class="brand__square"></span>
      <span class="brand__name">KOVE</span>
    </div>
    <div class="brand__sub">CONSTRUCTION</div>

    <div class="owner">
      <div class="owner__name">MARCUS TOLLIVER</div>
      <div class="owner__role">OWNER</div>
    </div>
    <div class="divider"></div>

    <ul class="contacts">
      <li>
        <svg viewBox="0 0 20 20" aria-hidden="true"><circle cx="10" cy="10" r="10" fill="#151515"/><path d="M7 5.5l2 2-1 1.3c.6 1.3 1.6 2.3 2.9 2.9l1.3-1 2 2-1.2 1.6c-3.6-.6-6.3-3.3-6.9-6.9z" fill="#fefdec"/></svg>
        <span>(555)203-7481</span>
      </li>
      <li>
        <svg viewBox="0 0 20 20" aria-hidden="true"><circle cx="10" cy="10" r="10" fill="#151515"/><rect x="5" y="6.5" width="10" height="7" fill="none" stroke="#fefdec" stroke-width="1.2"/><path d="M5 6.5l5 4 5-4" fill="none" stroke="#fefdec" stroke-width="1.2"/></svg>
        <span>kovecohomes@brindlemail.example</span>
      </li>
      <li>
        <svg viewBox="0 0 20 20" aria-hidden="true"><circle cx="10" cy="10" r="10" fill="#151515"/></svg>
        <span>kovecohomes</span>
      </li>
    </ul>
  </section>

  <section class="card card--back">
    <div class="back__border"></div>
    <div class="back__frame">
      <div class="back__name">KOVE</div>
      <div class="back__sub">CONSTRUCTION</div>
    </div>
  </section>
</body>
</html>
```